Velnimo.org
Brackwater Residents association
plz star rating....
in the back of the card it should have the following
K&T BULKWARE SUPPLIERS
847 HAZELMOOR ROAD
OLVERTON MA. 02946
we will like the back ground of the card to be red... our colors are red yellow and blue.

```html
<!DOCTYPE html>
<html lang="en">
<head>
<meta charset="utf-8">
<title>Velnimo.org Stationery Set</title>
<link href="https://fonts.googleapis.com/css2?family=Open+Sans:wght@400;600;700&display=swap" rel="stylesheet">
<style>
:root{
  --bg:#ece3d2;
  --paper:#ffffff;
  --blue:#1e9be0;
  --yellow:#f7e04a;
  --yellow-soft:#fbef9a;
  --ink:#6b7a86;
  --label:#7d6f5c;
  --faint:#e6f2fa;
}
*{margin:0;padding:0;box-sizing:border-box}
html,body{width:1200px;height:446px;overflow:hidden;background:var(--bg);font-family:"Open Sans",sans-serif}
.canvas{position:relative;width:1200px;height:446px}
.paper{position:absolute;background:var(--paper);box-shadow:0 2px 6px rgba(0,0,0,.18);overflow:hidden}
.label{position:absolute;font-size:7px;color:var(--label);letter-spacing:.3px;text-align:center}
.brand{color:var(--blue);font-weight:700;white-space:nowrap;display:flex;align-items:center;gap:3px}
.brand .dot{width:6px;height:6px;background:var(--yellow);border-radius:50%}
.tagline{color:var(--ink);font-size:4px;white-space:nowrap}
.small{font-size:4px;color:var(--ink);line-height:1.5}
.wave{position:absolute;left:0;bottom:0;width:100%}
.ghost{position:absolute;color:var(--faint);font-weight:700;white-space:nowrap}

.section-title{left:16px;top:77px;width:110px;text-align:left;font-size:7px}
.card{width:102px;height:50px}
.card-front{left:19px;top:161px}
.card-back{left:19px;top:228px;display:flex;flex-direction:column;justify-content:center;align-items:center}
.card-front .brand{position:absolute;left:8px;top:8px;font-size:8px}
.card-front .tagline{position:absolute;left:8px;top:20px;font-size:3.5px}
.card-front .small{position:absolute;right:6px;top:8px;text-align:right;font-size:3.5px}
.card-back .small{font-size:4px;text-align:center;font-weight:600}

.letterhead{width:228px;height:391px;top:17px}
.lh-1{left:151px}
.lh-2{left:403px}
.letterhead .brand{position:absolute;left:84px;top:20px;font-size:10px}
.letterhead .tagline{position:absolute;left:70px;top:35px}
.letterhead .contact{position:absolute;right:14px;top:14px;text-align:right}
.letterhead .ghost{left:40px;top:170px;font-size:26px}
.letterhead .footer{position:absolute;bottom:10px;width:100%;text-align:center;font-size:4px;color:var(--blue)}

.env{width:200px;height:90px}
.env-blue{left:666px;top:17px;background:var(--blue)}
.env-yellow{left:688px;top:108px;background:var(--yellow)}
.env-white{left:688px;top:221px}
.env-front{left:636px;top:318px;width:252px;height:96px}
.env-front .brand{position:absolute;left:12px;top:10px;font-size:9px}
.env-front .tagline{position:absolute;left:12px;top:23px}
</style>
</head>
<body>
<main class="canvas">

  <p class="label section-title">Business Card Design</p>

  <section class="paper card card-front">
    <div class="brand"><span class="dot"></span>Velnimo.org</div>
    <div class="tagline">Brackwater Residents association</div>
    <div class="small">Dana Merrow<br>President<br>(413) 555-0182</div>
    <svg class="wave" viewBox="0 0 102 10" preserveAspectRatio="none" height="10"><path d="M0 6 Q30 0 60 5 T102 3 V10 H0Z" fill="var(--yellow)"/><path d="M0 8 Q35 3 65 7 T102 6 V10 H0Z" fill="var(--blue)"/></svg>
  </section>
  <p class="label" style="left:19px;top:213px;width:102px">Business Card Front</p>

  <section class="paper card card-back">
    <div class="small">K&amp;T BULKWARE SUPPLIERS<br>847 HAZELMOOR ROAD<br>OLVERTON MA. 02946</div>
  </section>
  <p class="label" style="left:19px;top:280px;width:102px">Business Card Back</p>

  <section class="paper letterhead lh-1">
    <div class="brand"><span class="dot"></span>Velnimo.org</div>
    <div class="tagline">Brackwater Residents association</div>
    <div class="small contact">Phone (413) 555-0182<br>info@velnimo.org</div>
    <div class="ghost" aria-hidden="true">Velnimo.org</div>
    <svg class="wave" viewBox="0 0 228 40" preserveAspectRatio="none" height="40"><path d="M0 18 Q70 0 130 16 T228 10 V40 H0Z" fill="var(--yellow)"/><path d="M0 26 Q80 10 140 24 T228 20 V40 H0Z" fill="var(--blue)"/><path d="M0 32 Q90 20 150 30 T228 28 V40 H0Z" fill="var(--paper)"/></svg>
    <div class="footer">www.velnimo.org</div>
  </section>
  <p class="label" style="left:151px;top:412px;width:228px">Letterhead Option 1</p>

  <section class="paper letterhead lh-2">
    <div class="brand"><span class="dot"></span>Velnimo.org</div>
    <div class="tagline">Brackwater Residents association</div>
    <div class="ghost" aria-hidden="true">Velnimo.org</div>
    <svg class="wave" viewBox="0 0 228 40" preserveAspectRatio="none" height="40"><path d="M0 18 Q70 0 130 16 T228 10 V40 H0Z" fill="var(--yellow)"/><path d="M0 26 Q80 10 140 24 T228 20 V40 H0Z" fill="var(--blue)"/><path d="M0 32 Q90 20 150 30 T228 28 V40 H0Z" fill="var(--paper)"/></svg>
    <div class="footer">www.velnimo.org</div>
  </section>
  <p class="label" style="left:403px;top:412px;width:228px">Letterhead Option 2</p>

  <section class="paper env env-blue">
    <svg viewBox="0 0 200 90" width="200" height="90"><path d="M0 0 L100 42 L200 0 Z" fill="#4fb4ea"/></svg>
  </section>
  <section class="paper env env-yellow">
    <svg viewBox="0 0 200 90" width="200" height="90"><path d="M0 0 L100 42 L200 0 Z" fill="var(--yellow-soft)"/></svg>
  </section>
  <section class="paper env env-white">
    <svg viewBox="0 0 200 90" width="200" height="90"><path d="M0 0 L100 42 L200 0" fill="none" stroke="#dfe4e8"/></svg>
  </section>

  <section class="paper env env-front">
    <div class="brand"><span class="dot"></span>Velnimo.org</div>
    <div class="tagline">Brackwater Residents association</div>
    <svg class="wave" viewBox="0 0 252 20" preserveAspectRatio="none" height="20"><path d="M0 9 Q80 0 150 8 T252 5 V20 H0Z" fill="var(--yellow)"/><path d="M0 14 Q90 5 160 12 T252 10 V20 H0Z" fill="var(--blue)"/></svg>
  </section>
  <p class="label" style="left:636px;top:418px;width:252px">Envelope Options</p>

</main>
</body>
</html>
```